I need a business card for ALVA Holdings. We are a young startup based in New Zealand working in internet marketing and web development. The design should have some element connected to New Zealand, such as wave, koru or silver fern, just don't use a kiwi bird.

```html
<!DOCTYPE html>
<html lang="en">
<head>
<meta charset="utf-8">
<title>ALVA Holdings — Business Card</title>
<link href="https://fonts.googleapis.com/css2?family=Source+Sans+3:wght@400;600;700;800&display=swap" rel="stylesheet">
<style>
  :root {
    --page: #e5e5e5;
    --card-dark: #141414;
    --card-mid: #2a2a2a;
    --card-light: #3c3c3c;
    --brand-blue: #0f70bb;
    --brand-orange: #ea5a25;
    --text-light: #f2f2f2;
  }
  * { margin: 0; padding: 0; box-sizing: border-box; }
  html, body { width: 1200px; height: 1200px; overflow: hidden; }
  body {
    background: var(--page);
    font-family: "Source Sans 3", sans-serif;
    position: relative;
  }
  .card {
    position: absolute;
    left: 239px;
    width: 720px;
    height: 434px;
    border-radius: 16px;
    overflow: hidden;
    background: linear-gradient(150deg, var(--card-dark) 0%, var(--card-dark) 45%, var(--card-mid) 78%, var(--card-light) 100%);
  }
  .card--front { top: 148px; }
  .card--back { top: 616px; }

  /* front */
  .fern-decoration {
    position: absolute;
    left: 10px; top: 118px;
    width: 720px; height: 170px;
    border-radius: 0 100% 0 100%;
    transform: rotate(-27deg);
    background: linear-gradient(90deg, rgba(255,255,255,0.07) 0%, rgba(255,255,255,0.06) 55%, rgba(255,255,255,0.03) 100%);
  }
  .brand {
    position: absolute;
    color: var(--brand-blue);
    font-weight: 800;
    line-height: 1;
    text-align: center;
  }
  .brand__name { display: block; letter-spacing: 2px; }
  .brand__sub { display: block; font-weight: 700; }
  .card--front .brand { left: 0; right: 0; top: 96px; }
  .card--front .brand__name { font-size: 160px; }
  .card--front .brand__sub { font-size: 40px; letter-spacing: 26px; margin-top: 0; padding-left: 26px; }

  .front-web {
    position: absolute;
    left: 0; right: 0; top: 388px;
    display: flex; align-items: center; justify-content: center; gap: 14px;
    color: var(--text-light);
    font-size: 19px;
  }
  .front-web__rule { width: 68px; height: 3px; background: var(--brand-blue); }
  .front-web .hl-blue { color: var(--brand-blue); }
  .front-web .hl-orange { color: var(--brand-orange); }

  /* back */
  .koru-decoration {
    position: absolute;
    left: 400px; top: 8px;
    width: 330px; height: 330px;
    border-radius: 50%;
    background: radial-gradient(circle at 45% 55%, rgba(255,255,255,0.03) 0%, rgba(255,255,255,0.06) 45%, rgba(255,255,255,0.03) 75%, rgba(255,255,255,0.05) 100%);
  }
  .card--back .brand { left: 35px; top: 42px; text-align: left; }
  .card--back .brand__name { font-size: 104px; }
  .card--back .brand__sub { font-size: 28px; letter-spacing: 20px; margin-top: -4px; }

  .address {
    position: absolute; left: 35px; top: 200px;
    color: var(--text-light); font-size: 19px;
  }
  .contacts {
    position: absolute; left: 35px; top: 233px;
    list-style: none;
    color: var(--text-light); font-size: 19px;
  }
  .contacts li { display: flex; align-items: center; height: 25.5px; }
  .contacts .icon { width: 18px; height: 18px; margin-right: 18px; flex: none; }
  .contacts .social-dot {
    width: 17px; height: 17px; border-radius: 50%;
    background: var(--brand-orange); margin-right: 18px; flex: none;
  }
  .contacts .social-dot--second { margin-left: 12px; margin-right: 10px; }

  .waves { position: absolute; left: 0; top: 0; width: 720px; height: 434px; }

  .person {
    position: absolute; right: 43px; top: 336px;
    text-align: right; color: var(--text-light);
  }
  .person__name { font-size: 31px; font-weight: 700; line-height: 1; }
  .person__title { font-size: 18px; margin-top: 8px; }
</style>
</head>
<body>

<section class="card card--front">
  <div class="fern-decoration" role="img" aria-label="Faint silver fern frond sweeping diagonally behind the name"></div>
  <div class="brand">
    <span class="brand__name">ALVA</span>
    <span class="brand__sub">HOLDINGS</span>
  </div>
  <div class="front-web">
    <span class="front-web__rule"></span>
    <span>www.<span class="hl-blue">alva</span><span class="hl-orange">holdings</span>.com</span>
    <span class="front-web__rule"></span>
  </div>
</section>

<section class="card card--back">
  <div class="koru-decoration" role="img" aria-label="Faint koru spiral decoration"></div>

  <svg class="waves" viewBox="0 0 720 434" aria-hidden="true">
    <defs>
      <linearGradient id="bandFill" x1="0" y1="0" x2="1" y2="0">
        <stop offset="0" stop-color="#ea5a25"/>
        <stop offset="0.45" stop-color="#8a6673"/>
        <stop offset="0.8" stop-color="#2f6aa5"/>
        <stop offset="1" stop-color="#1070ba"/>
      </linearGradient>
      <linearGradient id="swoosh" x1="0" y1="0" x2="1" y2="0">
        <stop offset="0" stop-color="#1070ba"/>
        <stop offset="0.6" stop-color="#2e66a0"/>
        <stop offset="1" stop-color="#7a6a80"/>
      </linearGradient>
      <linearGradient id="topStroke" x1="0" y1="0" x2="1" y2="0">
        <stop offset="0" stop-color="#3b6ea5" stop-opacity="0.3"/>
        <stop offset="0.5" stop-color="#9a6560"/>
        <stop offset="1" stop-color="#ea5a25"/>
      </linearGradient>
    </defs>
    <path d="M0,335 C120,400 260,410 370,370 C470,330 560,272 650,264 C690,261 710,266 720,270 L720,434 L0,434 Z" fill="#161616"/>
    <path d="M0,379 C110,425 230,430 330,395 C420,362 480,318 560,304 C620,293 680,300 720,311 L720,434 L0,434 Z" fill="url(#bandFill)"/>
    <path d="M0,335 C110,382 250,396 365,378 C250,388 110,380 0,356 Z" fill="url(#swoosh)"/>
    <path d="M320,386 C460,330 560,266 650,261 C690,259 710,264 720,268" fill="none" stroke="url(#topStroke)" stroke-width="9"/>
  </svg>

  <div class="brand">
    <span class="brand__name">ALVA</span>
    <span class="brand__sub">HOLDINGS</span>
  </div>

  <p class="address">57 Tidewater Lane, Fernbay,&nbsp; Harbour City, NZ 1011</p>

  <ul class="contacts">
    <li>
      <svg class="icon" viewBox="0 0 20 20" aria-hidden="true"><path fill="#ea5a25" d="M2 7c0-2 3-4 8-4s8 2 8 4v1h-4V6.5c-1-.6-7-.6-8 0V8H2z"/><path fill="#ea5a25" d="M5 9h10l2 8H3z"/><circle cx="10" cy="13" r="2" fill="#141414"/></svg>
      555-0142-318
    </li>
    <li>
      <svg class="icon" viewBox="0 0 20 20" aria-hidden="true"><rect x="1" y="4" width="18" height="12" fill="#ea5a25"/><path d="M1 4l9 7 9-7M1 16l7-6M19 16l-7-6" stroke="#141414" stroke-width="1.5" fill="none"/></svg>
      hello@alvaholdings.com
    </li>
    <li>
      <svg class="icon" viewBox="0 0 20 20" aria-hidden="true"><g fill="none" stroke="#ea5a25" stroke-width="1.6"><circle cx="10" cy="10" r="8"/><ellipse cx="10" cy="10" rx="3.5" ry="8"/><path d="M2 10h16M3.5 6h13M3.5 14h13"/></g></svg>
      www.alvaholdings.com
    </li>
    <li>
      <span class="social-dot"></span>@marekvidal
      <span class="social-dot social-dot--second"></span>@marekvidal
    </li>
  </ul>

  <div class="person">
    <p class="person__name">Marek Vidal</p>
    <p class="person__title">Managing Director</p>
  </div>
</section>

</body>
</html>
```